Labels for my sauce bottles

I have designed the label- a few change suggestions are welcome<br/>but I basically need what is on the uploaded images- made high quality<br/>I don't have the programs to ensure it prints correctly and doesn't blur.<br/>I also have more labels to do- name, barcode and Nutritional Panel change- design/ concept stay the same<br/>dimensions are 190mm (long) x 75mm (High)

Font styles to use
Decorative
Script

Colors
ffc214

```html
<!DOCTYPE html>
<html lang="en">
<head>
<meta charset="utf-8">
<title>Ember Glaze – Blazin' Butternut label</title>
<link rel="stylesheet" href="https://fonts.googleapis.com/css2?family=Andika:wght@400;700&family=Alegreya:wght@400&display=swap">
<style>
  :root {
    --page-bg: #eeeeee;
    --label-black: #000000;
    --ember-orange: #b8521a;
    --ember-deep: #c9641c;
    --gold: #ffc214;
    --gold-text: #d9a21f;
    --title-white: #e8e8e8;
  }
  html, body {
    margin: 0;
    padding: 0;
    width: 1200px;
    height: 1200px;
    overflow: hidden;
    background: var(--page-bg);
  }
  .canvas {
    position: relative;
    width: 1200px;
    height: 1200px;
  }
  .sauce-label {
    position: absolute;
    left: 50px;
    top: 383px;
    width: 1100px;
    height: 434px;
    box-shadow: 0 18px 40px rgba(0,0,0,0.18);
  }
  .brand-name {
    font-family: "Andika", sans-serif;
    font-weight: 700;
    font-size: 40px;
    fill: var(--gold-text);
  }
  .tagline {
    font-family: "Alegreya", serif;
    font-size: 19px;
    letter-spacing: 1px;
    fill: var(--gold-text);
  }
  .product-name {
    font-family: "Andika", sans-serif;
    font-weight: 700;
    font-size: 80px;
    fill: var(--title-white);
  }
  .volume {
    font-family: "Andika", sans-serif;
    font-weight: 700;
    font-size: 28px;
    fill: var(--gold-text);
  }
</style>
</head>
<body>
<main class="canvas">
  <svg class="sauce-label" viewBox="0 0 1100 434" xmlns="http://www.w3.org/2000/svg" role="img" aria-label="Ember Glaze Blazin' Butternut sauce label, 250 ml">
    <defs>
      <linearGradient id="outer-fade" x1="0" y1="47" x2="0" y2="330" gradientUnits="userSpaceOnUse">
        <stop offset="0" stop-color="var(--ember-orange)"/>
        <stop offset="0.55" stop-color="#3a1a08"/>
        <stop offset="1" stop-color="var(--label-black)"/>
      </linearGradient>
      <linearGradient id="arch-glow" x1="0" y1="47" x2="0" y2="206" gradientUnits="userSpaceOnUse">
        <stop offset="0" stop-color="var(--label-black)"/>
        <stop offset="0.55" stop-color="#1a0a03"/>
        <stop offset="1" stop-color="var(--ember-deep)"/>
      </linearGradient>
      <path id="tagline-arc" d="M395 150 Q550 250 705 150"/>
    </defs>

    <rect class="label-base" width="1100" height="434" fill="var(--label-black)"/>

    <path class="outer-band" fill="url(#outer-fade)"
      d="M0 47 H280 Q312 47 330 90 C370 180 450 206 550 206 C650 206 730 180 770 90 Q788 47 820 47 H1100 V434 H0 Z"/>
    <path class="arch-field" fill="url(#arch-glow)"
      d="M280 47 Q312 47 330 90 C370 180 450 206 550 206 C650 206 730 180 770 90 Q788 47 820 47 Z"/>

    <path class="gold-rule" fill="none" stroke="var(--gold)" stroke-width="4"
      d="M0 47 H280 Q312 47 330 90 C370 180 450 206 550 206 C650 206 730 180 770 90 Q788 47 820 47 H1100"/>

    <circle class="brand-dot" cx="388" cy="87" r="9" fill="var(--gold-text)"/>
    <text class="brand-name" x="560" y="100" text-anchor="middle">Ember Glaze</text>

    <text class="tagline"><textPath href="#tagline-arc" startOffset="50%" text-anchor="middle">- small batch craft sauce -</textPath></text>

    <text class="product-name" x="550" y="280" text-anchor="middle">Blazin'</text>
    <text class="product-name" x="550" y="370" text-anchor="middle">Butternut</text>
    <text class="volume" x="550" y="418" text-anchor="middle">250 ml</text>
  </svg>
</main>
</body>
</html>
```